Business Card - high end, modern health care

Hey designers!

We need a double sided business card for the boutique, cutting edge physical therapy rehabilitation centre in Sydney's Northern Beaches.

With the most qualified physios in the area The Harbourline Motion Clinic does what other physiotherapy practices do not, we take our time with our patients giving them longer appointments, better physios and therefor faster results!

We guarantee that the service people receive at THMC will be unparalleled.

Hence we need a business card to reflect our modern, boutique, high end service. The final design needs to reflect that we are in a class of our own yet with the feel of beachside retreat.

Below I have attached our logo in both blue on white and white on blue. The exact colour is;
and the font that we have used in our logo is Tex Gyre Aventador.

I like the idea of the blue as the main colour as it is more eye catching and our signage onto the main road will be in this blue and in the interest of consistency across marketing the blue needs to be a part of the design. However I would appreciate a few designs onto a wooden background as this is a visual theme within the fitout of the practice.

The design needs to be of standard size (91x55mm).

Target Market(s)

We target people who have an end outcome in mind and those who have had poor experiences with other providers and ensure that everyone gets the care that they deserve with a premium service that is tailored to the individuals circumstances. As a premium service, the target market is highly educated, business and tech savvy with the additional target market of elderly people who have self funded their retirement and see value in paying for the best ongoing rehabilitation to maintain independence.

Industry/Entity Type

Physical Therapy

Contact Information for Business Card

Name, designation( Titled Musculoskeletal Physiotherapist... there will also be those in the company that have multiple designations ie 5 or 6 words long), phone number, email, facebook, instagram, address

Font styles to use
Sans Serif

Colors

Designer to choose colors to be used in the design.

Requirements
Must have
• Front - The logo as large as possible, blue or wooden theme, and all of the important details.
• Back - A blank space/lines on which to write appointment times (no "Appointment, date, time" etc.)
Nice to have
• facebook url
• logos for facebook and instagram
• Mini logos for the phone and email?

```html
<!DOCTYPE html>
<html lang="en">
<head>
<meta charset="utf-8">
<title>The Harbourline Motion Clinic – Business Card</title>
<link href="https://fonts.googleapis.com/css2?family=Roboto:wght@300;400;700&display=swap" rel="stylesheet">
<style>
  :root {
    --brand-blue: #1663b6;
    --brand-blue-dark: #0f529c;
    --card-white: #f7f7f7;
    --back-white: #ffffff;
    --ink-grey: #5a5a5a;
    --rule-grey: #8a8a8a;
    --stage: #e4e2de;
  }
  * { box-sizing: border-box; margin: 0; padding: 0; }
  html, body { width: 1200px; height: 911px; overflow: hidden; }
  body {
    background: var(--stage);
    font-family: "Roboto", Arial, sans-serif;
    display: flex;
    flex-direction: column;
    align-items: center;
    justify-content: center;
    gap: 40px;
  }
  .card {
    position: relative;
    width: 640px;
    height: 387px;
    border-radius: 18px;
    overflow: hidden;
    box-shadow: 0 3px 10px rgba(0,0,0,.18);
  }

  /* Front */
  .card--front { background: var(--card-white); }
  .front__band {
    position: absolute; left: 0; top: 0; right: 0; height: 96px;
    background: linear-gradient(180deg, var(--brand-blue) 0%, var(--brand-blue-dark) 100%);
  }
  .holder {
    position: absolute; right: 40px; top: 22px;
    text-align: right; color: #fff;
  }
  .holder__name { font-weight: 700; font-size: 26px; letter-spacing: .5px; line-height: 1.1; }
  .holder__role { font-weight: 400; font-size: 16px; letter-spacing: .5px; margin-top: 4px; }

  .brand-mark {
    position: absolute; left: 78px; top: 52px;
    width: 190px; height: 190px; border-radius: 50%;
    background: var(--brand-blue);
    border: 6px solid var(--card-white);
  }
  .brand-name {
    position: absolute; left: 40px; top: 258px; width: 270px;
    text-align: center;
    color: var(--brand-blue);
    font-weight: 700; font-size: 22px; line-height: 1.2; letter-spacing: .5px;
    text-transform: uppercase;
  }

  .contact {
    position: absolute; right: 40px; top: 126px;
    list-style: none; text-align: right;
    color: var(--ink-grey); font-size: 15px; line-height: 25px;
  }
  .contact li { display: flex; justify-content: flex-end; align-items: center; gap: 8px; }
  .contact .gap { height: 10px; }
  .contact svg { width: 14px; height: 14px; flex: none; }
  .contact .no-icon { padding-right: 22px; }

  /* Back */
  .card--back { background: var(--back-white); }
  .back__brand {
    position: absolute; right: 40px; top: 34px;
    display: flex; align-items: center; gap: 12px;
  }
  .back__dot { width: 42px; height: 42px; border-radius: 50%; background: var(--brand-blue); }
  .back__name {
    color: var(--brand-blue); font-weight: 700; font-size: 20px; line-height: 1.15;
    text-transform: uppercase; letter-spacing: .5px;
  }
  .write-lines { position: absolute; left: 40px; right: 40px; top: 120px; }
  .write-lines__row {
    display: flex; gap: 24px;
    height: 40px;
  }
  .write-lines__line { flex: 1; border-bottom: 1px solid var(--rule-grey); }
</style>
</head>
<body>

  <section class="card card--front" aria-label="Business card front">
    <div class="front__band"></div>
    <div class="holder">
      <p class="holder__name">DANIEL REEVE</p>
      <p class="holder__role">CEO/FOUNDER</p>
    </div>

    <div class="brand-mark"></div>
    <p class="brand-name">The Harbourline<br>Motion Clinic</p>

    <ul class="contact">
      <li class="no-icon">214 Seacliff Avenue</li>
      <li class="no-icon">Dee Why NSW 2099</li>
      <li class="gap"></li>
      <li>612 804 3917
        <svg viewBox="0 0 24 24" aria-hidden="true"><path fill="var(--brand-blue)" d="M6.6 10.8a15.1 15.1 0 0 0 6.6 6.6l2.2-2.2a1 1 0 0 1 1-.25 11.4 11.4 0 0 0 3.6.57 1 1 0 0 1 1 1V20a1 1 0 0 1-1 1A17 17 0 0 1 3 4a1 1 0 0 1 1-1h3.5a1 1 0 0 1 1 1c0 1.25.2 2.45.57 3.57a1 1 0 0 1-.25 1z"/></svg>
      </li>
      <li>daniel@harbourlinemotion.com
        <svg viewBox="0 0 24 24" aria-hidden="true"><rect x="2" y="5" width="20" height="14" rx="2" fill="var(--brand-blue)"/><path d="M3 6l9 7 9-7" fill="none" stroke="#fff" stroke-width="1.8"/></svg>
      </li>
      <li>www.harbourlinemotion.com
        <svg viewBox="0 0 24 24" aria-hidden="true"><circle cx="12" cy="12" r="10" fill="var(--brand-blue)"/><path d="M2 12h20M12 2c3 3 3 17 0 20M12 2c-3 3-3 17 0 20" fill="none" stroke="#fff" stroke-width="1.5"/></svg>
      </li>
      <li>/harbourlinemotion
        <svg viewBox="0 0 24 24" aria-hidden="true"><rect x="3" y="3" width="18" height="18" rx="3" fill="var(--brand-blue)"/></svg>
      </li>
      <li>@harbourlinemotion
        <svg viewBox="0 0 24 24" aria-hidden="true"><rect x="3" y="3" width="18" height="18" rx="3" fill="var(--brand-blue)"/></svg>
      </li>
    </ul>
  </section>

  <section class="card card--back" aria-label="Business card back">
    <div class="back__brand">
      <div class="back__dot"></div>
      <p class="back__name">The Harbourline<br>Motion Clinic</p>
    </div>

    <div class="write-lines">
      <div class="write-lines__row"><div class="write-lines__line"></div></div>
      <div class="write-lines__row"><div class="write-lines__line"></div><div class="write-lines__line"></div></div>
      <div class="write-lines__row"><div class="write-lines__line"></div></div>
      <div class="write-lines__row"><div class="write-lines__line"></div></div>
      <div class="write-lines__row"><div class="write-lines__line"></div></div>
      <div class="write-lines__row"><div class="write-lines__line"></div></div>
    </div>
  </section>

</body>
</html>
```